M&A Advisory firm needs elegant and powerful letterhead

We need a powerful but elegant letterhead to engage with the international financial industry.

Target Market(s)

New York and International Financial Industry

Industry/Entity Type

Finance

Font styles to use
Other font styles liked:
• Poppins

Requirements
Must have
• 482 W 17th Avenue 9th Floor New York, NY 10384 O: +1 (555) 804 2176 F: +1 (555) 804 2193

```html
<!DOCTYPE html>
<html lang="en">
<head>
<meta charset="utf-8">
<title>Meriden Letterhead</title>
<link rel="stylesheet" href="https://fonts.googleapis.com/css2?family=Poppins:wght@500;600&family=Quicksand:wght@400&family=Open+Sans:wght@400;600&family=Lato:wght@400&family=Questrial&display=swap">
<style>
  :root {
    --brand-blue: #0b4f96;
    --band-grey: #e6e6e8;
    --rule-grey: #8a8a8c;
    --text-grey: #8c8c8e;
    --body-grey: #9a9a9c;
    --stage: #ebecee;
    --paper: #ffffff;
    --ink: #1a1a1a;
  }
  * { margin: 0; padding: 0; box-sizing: border-box; }
  html, body {
    width: 1068px; height: 1200px; overflow: hidden;
    background: var(--stage);
  }
  .sheet {
    position: absolute; left: 106px; top: 0;
    width: 855px; height: 1200px;
    background: var(--paper);
    overflow: hidden;
  }
  .header-art, .footer-art { position: absolute; left: 0; }
  .header-art { top: 0; }
  .footer-art { top: 1130px; }

  .brand {
    position: absolute; left: 43px; top: 68px;
    display: flex; align-items: center; gap: 14px;
  }
  .brand-dot {
    width: 40px; height: 40px; border-radius: 50%;
    background: var(--brand-blue);
  }
  .brand-name {
    font-family: "Poppins", sans-serif; font-weight: 500;
    font-size: 46px; line-height: 1; letter-spacing: 1px;
    color: var(--brand-blue);
  }

  .contact-lines { position: absolute; left: 664px; top: 80px; }
  .contact-line {
    display: flex; align-items: center; gap: 5px;
    height: 20px; margin-bottom: 14px;
    font-family: "Open Sans", sans-serif; font-size: 15px;
    color: #6f6f72;
  }
  .contact-icon { width: 20px; height: 20px; flex: none; }

  .sender {
    position: absolute; left: 63px; top: 312px;
    font-family: "Quicksand", sans-serif; color: var(--text-grey);
    font-size: 14.5px;
  }
  .sender-name {
    font-family: "Poppins", sans-serif; font-weight: 600;
    font-size: 25px; letter-spacing: 0.3px; color: #9a9a9c;
    line-height: 30px; margin-bottom: 8px;
  }
  .sender p { line-height: 26px; }
  .sender .address { line-height: 20px; margin-top: 2px; }

  .letter-date {
    position: absolute; right: 58px; top: 418px;
    font-family: "Open Sans", sans-serif; font-weight: 600;
    font-size: 16px; color: var(--text-grey);
  }

  .letter-body {
    position: absolute; left: 58px; top: 473px; width: 739px;
    font-family: "Questrial", sans-serif; font-size: 14.4px;
    line-height: 18.7px; color: var(--body-grey);
    text-align: justify;
  }
  .letter-body p + p { margin-top: 18.7px; }
  .letter-body p.spaced { margin-top: 37px; }

  .signatory {
    position: absolute; left: 561px; top: 850px;
    font-family: "Questrial", sans-serif; font-size: 21px;
    color: var(--body-grey);
  }
  .signature-area {
    position: absolute; left: 579px; top: 894px;
    width: 150px; height: 95px;
    background: linear-gradient(180deg, #f4f4f5, #ececed);
  }

  .footer-address {
    position: absolute; left: 504px; top: 1143px;
    font-family: "Lato", sans-serif; font-size: 14.3px;
    color: #ffffff; white-space: nowrap;
  }
</style>
</head>
<body>
  <main class="sheet">
    <svg class="header-art" width="855" height="170" viewBox="0 0 855 170" aria-hidden="true">
      <polygon points="0,36 345,36 299,160 0,160" fill="var(--band-grey)"/>
      <polygon points="352,36 360,36 315,160 308,160" fill="var(--brand-blue)"/>
      <polygon points="368,36 375,36 331,160 323,160" fill="var(--brand-blue)"/>
    </svg>

    <div class="brand">
      <span class="brand-dot"></span>
      <span class="brand-name">MERIDEN</span>
    </div>

    <div class="contact-lines">
      <div class="contact-line">
        <svg class="contact-icon" viewBox="0 0 20 20" aria-hidden="true">
          <rect width="20" height="20" rx="3" fill="var(--brand-blue)"/>
          <path d="M6.2 4.5l2 .3.8 2.8-1.3 1c.7 1.5 1.8 2.6 3.3 3.3l1-1.3 2.8.8.3 2c-.2.8-.9 1.3-1.7 1.2C9 14.3 5.7 11 5.4 6.2c-.1-.8.4-1.5.8-1.7z" fill="#fff"/>
        </svg>
        <span>+1 (555) 804 2176</span>
      </div>
      <div class="contact-line">
        <svg class="contact-icon" viewBox="0 0 20 20" aria-hidden="true">
          <rect width="20" height="20" rx="3" fill="var(--brand-blue)"/>
          <rect x="6.5" y="4" width="7" height="4" fill="none" stroke="#fff" stroke-width="1.3"/>
          <rect x="4" y="8" width="12" height="6" rx="1" fill="none" stroke="#fff" stroke-width="1.3"/>
          <rect x="6.5" y="11.5" width="7" height="4.5" fill="var(--brand-blue)" stroke="#fff" stroke-width="1.3"/>
        </svg>
        <span>+1 (555) 804 2193</span>
      </div>
    </div>

    <section class="sender">
      <h1 class="sender-name">DANA WHITFIELD</h1>
      <p>0198-372-645</p>
      <p>hello@sampledomain.com</p>
      <p class="address">5678 Elm Park Rd. Suite<br>410 Austin, TX 0000</p>
    </section>

    <p class="letter-date">12 December, 2023</p>

    <article class="letter-body">
      <p>Lorem ipsum dolor sit amet, consectetuer adipiscing elit, sed diam nonummy nibh euismod tincidunt ut laoreet dolore magna aliquam erat volutpat. Ut wisi enim ad minim veniam, quis nostrud exerci tation ullamcorper suscipit lobortis nisl ut aliquip ex ea commodo consequat. Duis autem vel eum iriure dolor in hendrerit in vulputate velit esse molestie consequat, vel illum dolore eu feugiat nulla facilisis at vero eros et accumsan et iusto odio dignissim qui blandit praesent luptatum zzril delenit augue duis dolore te feugait nulla facilisi.</p>
      <p>Lorem ipsum dolor sit amet, cons ectetuer adipiscing elit, sed diam nonummy nibh euismod tincidunt ut laoreet dolore magna aliquam erat volutpat. Ut wisi enim ad minim veniam, quis nostrud exerci tation ullamcorper suscipit lobortis nisl ut aliquip ex ea commodo consequat.<br>Lorem ipsum dolor sit amet, consectetuer adipiscing elit, sed diam nonummy nibh euismod tincidunt ut laoreet dolore magna aliquam erat</p>
      <p class="spaced">Lorem ipsum dolor sit amet, cons ectetuer adipiscing elit, sed diam nonummy nibh euismod tincidunt ut laoreet dolore magna aliquam erat volutpat. Ut wisi enim ad minim veniam, quis nostrud exerci tation ullamcorper suscipit lobortis nisl ut aliquip ex ea commodo consequat. Lorem ipsum dolor sit zamet, consectetuer adipiscing elit, sed diam nonummy nibh euismod tincidunt.</p>
    </article>

    <p class="signatory">Managing Director</p>
    <div class="signature-area" role="img" aria-label="Handwritten signature of the managing director"></div>

    <svg class="footer-art" width="855" height="45" viewBox="0 0 855 45" aria-hidden="true">
      <polygon points="0,37 464,37 462,42 0,42" fill="var(--rule-grey)"/>
      <polygon points="502,4 855,4 855,42 466,42" fill="var(--brand-blue)"/>
    </svg>
    <p class="footer-address">482 W 17th Avenue 9th Floor New York, NY 10384</p>
  </main>
</body>
</html>
```